Sleek, Professional Business Card Design Needed

Business Cards - Logo Attached.

We are a solar consulting company. We are national and want our cards to represent the professional high quality products that we offer.

Industry/Entity Type

Business

Contact Information for Business Card

n/a

Requirements
Must have
• Design
• Name
• Position
• Number
• Email
• Address
Should not have
• Not be too crowded

```html
<!DOCTYPE html>
<html lang="en">
<head>
<meta charset="utf-8">
<title>Sunridge Energy – Business Card</title>
<link rel="stylesheet" href="https://fonts.googleapis.com/css2?family=Open+Sans:wght@400;600;700&display=swap">
<style>
  :root {
    --backdrop: #07425f;
    --card-blue: #0b93d0;
    --deep-blue: #0a86c6;
    --leaf-green: #8cc63f;
    --pale-green: #c9df6b;
    --paper: #ffffff;
  }
  * { margin: 0; padding: 0; box-sizing: border-box; }
  html, body {
    width: 1200px; height: 1000px; overflow: hidden;
    background: var(--backdrop);
    font-family: "Open Sans", Arial, sans-serif;
  }
  .business-card {
    position: absolute; left: 150px; top: 243px;
    width: 900px; height: 514px;
    border-radius: 52px; overflow: hidden;
    box-shadow: 0 18px 40px rgba(0,0,0,0.3);
  }
  .card-shapes { position: absolute; inset: 0; }
  .brand {
    position: absolute; left: 40px; top: 110px; width: 345px;
    text-align: center; color: var(--deep-blue);
    font-weight: 600; font-size: 40px; line-height: 1.1; letter-spacing: 1px;
  }
  .brand-ring {
    width: 150px; height: 150px; margin: 0 auto 26px;
    border: 12px solid var(--leaf-green); border-radius: 50%;
  }
  .brand-sub { font-size: 26px; letter-spacing: 3px; }
  .holder {
    position: absolute; right: 36px; top: 74px; text-align: right; color: var(--paper);
  }
  .holder-name { font-size: 36px; font-weight: 400; letter-spacing: 2px; }
  .holder-name strong { font-weight: 700; }
  .holder-role { font-size: 20px; font-weight: 700; color: var(--leaf-green); letter-spacing: 2px; margin-top: 2px; }
  .contacts { position: absolute; right: 32px; top: 290px; list-style: none; color: var(--paper); }
  .contact {
    display: flex; align-items: center; justify-content: flex-end;
    font-size: 22px; font-weight: 700; height: 38px; text-align: right;
  }
  .contact.address { height: auto; margin-top: 18px; align-items: flex-start; line-height: 33px; }
  .contact-icon {
    width: 32px; height: 32px; margin-left: 16px; flex: none;
    border-radius: 50%; background: var(--leaf-green);
    display: flex; align-items: center; justify-content: center;
  }
</style>
</head>
<body>
  <main class="business-card">
    <svg class="card-shapes" width="900" height="514" viewBox="0 0 900 514">
      <rect width="900" height="514" fill="var(--card-blue)"/>
      <path d="M338 0 Q 660 257 322 514" fill="none" stroke="var(--pale-green)" stroke-width="26"/>
      <path d="M326 0 Q 640 257 312 514" fill="none" stroke="var(--leaf-green)" stroke-width="10"/>
      <path d="M318 0 Q 625 257 305 514" fill="none" stroke="var(--deep-blue)" stroke-width="14"/>
      <path d="M0 0 H310 Q 612 257 298 514 H0 Z" fill="var(--paper)"/>
    </svg>

    <div class="brand">
      <div class="brand-ring"></div>
      <div class="brand-name">SUNRIDGE</div>
      <div class="brand-sub">ENERGY</div>
    </div>

    <header class="holder">
      <h1 class="holder-name">DANA <strong>MERCER</strong></h1>
      <p class="holder-role">OWNER</p>
    </header>

    <ul class="contacts">
      <li class="contact">5550 284 176
        <span class="contact-icon"><svg width="18" height="18" viewBox="0 0 24 24"><path d="M6.6 10.8a15 15 0 0 0 6.6 6.6l2.2-2.2a1 1 0 0 1 1-.25 11 11 0 0 0 3.6.6 1 1 0 0 1 1 1V20a1 1 0 0 1-1 1A17 17 0 0 1 3 4a1 1 0 0 1 1-1h3.5a1 1 0 0 1 1 1 11 11 0 0 0 .6 3.6 1 1 0 0 1-.25 1z" fill="#fff"/></svg></span>
      </li>
      <li class="contact">dana.mercer@mail.com
        <span class="contact-icon"><svg width="18" height="18" viewBox="0 0 24 24"><rect x="3" y="6" width="18" height="12" rx="1.5" fill="none" stroke="#fff" stroke-width="2"/><path d="M3 7l9 6 9-6" fill="none" stroke="#fff" stroke-width="2"/></svg></span>
      </li>
      <li class="contact">www.sunridgeenergy.com
        <span class="contact-icon"><svg width="18" height="18" viewBox="0 0 24 24"><circle cx="12" cy="12" r="9" fill="none" stroke="#fff" stroke-width="2"/><path d="M3 12h18M12 3c3 3 3 15 0 18M12 3c-3 3-3 15 0 18" fill="none" stroke="#fff" stroke-width="1.6"/></svg></span>
      </li>
      <li class="contact address"><span>4821 Harbor Crest Blvd #210<br>Lakeview, FL 33010</span>
        <span class="contact-icon"><svg width="18" height="18" viewBox="0 0 24 24"><path d="M12 2a7 7 0 0 0-7 7c0 5 7 13 7 13s7-8 7-13a7 7 0 0 0-7-7z" fill="#fff"/><circle cx="12" cy="9" r="2.6" fill="var(--leaf-green)"/></svg></span>
      </li>
    </ul>
  </main>
</body>
</html>
```